website design for Velmora Carworks llc. an automotive Dry Ice detailling and cleaning business.

We need a website designed for an automotive detailing/cleaning company. I would like a grayscale style with the chosen colors to accent/highlight. We use super dry, compressed air to propel precisely processed, uniform particles of dry ice to clean and/or remove dirt and contaminants form vehicles concentrating mainly on undercarriage, engine bay and wheels/wheel wells. This process prevents water/moisture getting into areas of the vehicle you don't want it.

Target Market(s)

vehicle owners with luxury and/or collector cars

Industry/Entity Type

automotive dry ice detailing and cleaning

Coding

Coded - Design and coding required

Number of Pages Required

2 page

Font styles to use
Sans Serif

Colors
0054AA
0677BA
7BADD7
CADEEF
E8F1F8
00AB8E
00BBA5
67D7C9
C6EFE9
E9F9F6
EB3D1F
EC4F4E
F09395
F8D3D4
FCEDEE

Requirements
Must have
• logo prominently displayed on a darker background area. Links to social media and other businesses I am associated with. Photos and short video, sync with social so last (how many?3,5?) posts automatically sync with/show up on website.
Nice to have
• mostly grayscale with chosen colors to accentuate or for attention, excitement

```html
<!DOCTYPE html>
<html lang="en">
<head>
<meta charset="utf-8">
<title>Velmora Carworks – Automotive Detailing and Cleaning</title>
<link rel="stylesheet" href="https://fonts.googleapis.com/css2?family=Roboto:ital,wght@0,300;0,400;0,500;0,700;0,900;1,400&display=swap">
<style>
:root{
  --blue-deep:#0054AA;
  --blue:#0677BA;
  --blue-soft:#7BADD7;
  --blue-pale:#CADEEF;
  --blue-mist:#E8F1F8;
  --red:#EB3D1F;
  --red-soft:#EC4F4E;
  --ink:#1f2a44;
  --text:#555c66;
  --white:#ffffff;
  --photo-dark:#3a3d42;
  --photo-mid:#6b6f75;
}
*{box-sizing:border-box;margin:0;padding:0}
html,body{width:1200px;height:3846px;overflow:hidden;background:var(--white)}
body{font-family:"Roboto",Arial,sans-serif;color:var(--ink);position:relative}
.page{position:relative;width:1200px;height:3846px;overflow:hidden}
.abs{position:absolute}

/* header */
.site-header{position:absolute;left:0;top:0;width:1200px;height:95px;background:var(--white);z-index:5}
.brand{position:absolute;display:flex;align-items:center;gap:10px}
.brand-mark{width:34px;height:34px;border-radius:50%;background:var(--red);flex:none}
.brand-name{font-weight:700;color:var(--blue-deep);font-size:22px;line-height:1.05}
.site-header .brand{left:108px;top:22px}
.main-nav{position:absolute;top:38px;left:0;font-size:14px;text-transform:uppercase;color:#333}
.main-nav a{position:absolute;white-space:nowrap;text-decoration:none;color:#333}
.main-nav a.active{color:var(--red);font-weight:500}
.phone-pill{position:absolute;left:918px;top:27px;width:180px;height:42px;border-radius:21px;background:var(--blue);color:var(--white);font-size:14px;font-weight:700;display:flex;align-items:center;justify-content:center;gap:8px}

/* hero */
.hero{position:absolute;left:0;top:95px;width:1200px;height:639px;overflow:hidden}
.hero-photo{position:absolute;left:0;top:0;width:1200px;height:639px;background:linear-gradient(90deg,#55595f 0%,#8a8d91 45%,#3b3e43 55%,#2a2c30 100%)}
.hero-shape{position:absolute;left:0;top:0}
.hero-copy{position:absolute;left:105px;top:175px;color:var(--white)}
.hero-kicker{font-size:22px;letter-spacing:2px;font-weight:400}
.hero-title{font-size:40px;font-weight:700;line-height:43px;margin-top:10px;text-transform:uppercase}
.hero-title span{font-weight:400;display:block}
.hero-lede{font-size:15.5px;line-height:22px;margin-top:18px;width:400px}
.btn{position:absolute;height:47px;border-radius:24px;font-size:15px;font-weight:700;text-transform:uppercase;display:flex;align-items:center;justify-content:center;gap:6px;color:var(--white)}
.btn-outline{border:2px solid var(--white)}
.btn-red{background:var(--red)}
.slider-arrow{position:absolute}

/* section titles */
.sec-title{position:absolute;left:0;width:1200px;text-align:center}
.sec-kicker{font-size:20px;font-weight:400;text-transform:uppercase;letter-spacing:-.3px}
.sec-heading{font-size:36px;font-weight:700;text-transform:uppercase;line-height:40px}
.sec-rule{width:56px;height:3px;background:var(--blue-deep);margin:10px auto 0}

/* services */
.service-card{position:absolute;overflow:hidden;border-radius:6px;color:var(--white);text-align:center}
.service-card .photo{position:absolute;inset:0}
.service-card h3{position:absolute;left:0;right:0;bottom:18px;font-size:17px;font-weight:700;line-height:22px;text-transform:uppercase}
.service-featured{position:absolute;left:416px;top:906px;width:360px;height:328px;border-radius:6px;background:linear-gradient(160deg,#0a5fb0,#0b4a9c);color:var(--white);text-align:center;box-shadow:0 10px 24px rgba(0,40,100,.25)}
.service-featured h3{font-size:22px;font-weight:700;line-height:23px;text-transform:uppercase;margin-top:78px}
.service-featured p{font-size:13.5px;line-height:25px;margin:12px 46px 0}
.service-featured .btn{left:92px;top:231px;width:180px;height:40px;font-size:14px}

/* company */
.company{position:absolute;left:0;top:1313px;width:1200px;height:617px;background:linear-gradient(90deg,#e2442a 0%,#a14270 38%,#2a55a8 65%,#0b4aa2 100%)}
.company-oval{position:absolute;left:118px;top:36px;width:468px;height:520px;border-radius:50%;border:4px solid var(--white);padding:8px}
.company-oval .photo{width:100%;height:100%;border-radius:50%;background:linear-gradient(180deg,#6f7378 0%,#4d5055 48%,#e9e9e9 49%,#b8babd 52%,#8e3b3a 80%,#8a8d91 100%)}
.company-copy{position:absolute;left:618px;top:88px;color:var(--white);width:470px}
.company-copy .sec-kicker{font-size:20px}
.company-copy .sec-heading{font-size:35px;margin-top:2px}
.company-copy p.lede{font-size:14.5px;line-height:25px;margin-top:22px}
.feature{position:absolute;left:0;display:flex;gap:18px;align-items:flex-start}
.feature h4{font-size:18px;font-weight:500}
.feature p{font-size:12.5px;margin-top:4px}

/* gallery */
.shot{position:absolute;top:2124px;width:270px;height:192px;border-radius:4px;overflow:hidden}
.shot .photo{position:absolute;inset:0}
.shot .label{position:absolute;left:0;right:0;bottom:0;height:46px;padding:14px 0 0 28px;font-size:17px;font-weight:700;color:var(--white)}
.label.before{background:rgba(11,74,162,.88)}
.label.after{background:rgba(235,61,31,.82)}
.dots{position:absolute;top:2357px;left:578px;display:flex;gap:16px}
.dots i{width:11px;height:11px;border-radius:50%;background:var(--blue-soft);display:block}
.dots i.on{background:var(--red)}

/* testimonials */
.testimonials{position:absolute;left:0;top:2437px;width:1200px;height:515px;background:var(--blue-mist)}
.quote-card{position:absolute;top:2592px;width:454px;height:240px;background:var(--white);border-radius:6px}
.quote-card blockquote{position:absolute;left:44px;top:38px;width:385px;font-size:14px;line-height:26px;font-style:italic;color:#777}
.reviewer{position:absolute;left:44px;top:148px;display:flex;align-items:center;gap:10px}
.avatar{width:46px;height:46px;border-radius:50%;background:var(--blue-pale)}
.reviewer b{display:block;font-size:15.5px;font-weight:500;color:var(--blue-deep)}
.stars{color:#f5b400;font-size:17px;letter-spacing:2px}
.quote-mark{position:absolute;right:38px;bottom:18px;font-size:84px;line-height:60px;color:#d6dbe6;font-weight:900;font-family:Georgia,serif}

/* contact */
.contact{position:absolute;left:0;top:2952px;width:1200px;height:526px;overflow:hidden}
.contact .photo{position:absolute;inset:0;background:linear-gradient(120deg,#2a2d34 0%,#3d3f46 40%,#c21f1a 75%,#7e1512 100%)}
.contact-copy{position:absolute;left:115px;top:92px;color:var(--white)}
.contact-copy .sec-kicker{font-size:17px}
.contact-copy .sec-heading{font-size:35px;margin-top:0}
.contact-copy p{font-size:16px;line-height:26px;margin-top:12px;width:410px}
.contact-line{position:absolute;left:0;display:flex;align-items:center;gap:20px;font-size:18px;line-height:30px;font-weight:500}
.icon-disc{width:58px;height:58px;border-radius:50%;background:var(--red-soft);display:flex;align-items:center;justify-content:center;flex:none}

/* footer */
.site-footer .brand{left:110px;top:3580px}
.site-footer .brand-mark{width:40px;height:40px}
.site-footer .brand-name{font-size:26px}
.foot-col{position:absolute;top:3542px}
.foot-col h5{font-size:18px;font-weight:700;color:var(--blue-deep);text-transform:uppercase}
.foot-col ul{list-style:none;margin-top:14px}
.foot-col li{font-size:14px;color:#333;line-height:28px}
.foot-contact{display:flex;gap:12px;font-size:14px;line-height:26px;color:#333;margin-top:12px;align-items:flex-start}
.small-disc{width:34px;height:34px;border-radius:50%;background:var(--red-soft);display:flex;align-items:center;justify-content:center;flex:none}
.socials{display:flex;gap:8px;margin-top:18px}
.socials i{width:34px;height:34px;border-radius:50%;background:var(--red-soft);display:block}
.copyright{position:absolute;left:0;top:3773px;width:1200px;height:73px;background:#eef1f7;text-align:center;font-size:13px;line-height:73px;color:#444}
</style>
</head>
<body>
<div class="page">

<header class="site-header">
  <div class="brand"><span class="brand-mark"></span><span class="brand-name">Velmora<br>Carworks</span></div>
  <nav class="main-nav">
    <a class="active" style="left:331px">About Us</a>
    <a style="left:456px">Services</a>
    <a style="left:572px">Our Work</a>
    <a style="left:699px">Pricing</a>
    <a style="left:805px">Contact</a>
  </nav>
  <div class="phone-pill">
    <svg width="18" height="18" viewBox="0 0 24 24" fill="#fff"><path d="M6.6 10.8a15.1 15.1 0 0 0 6.6 6.6l2.2-2.2c.3-.3.7-.4 1-.2 1.1.4 2.3.6 3.6.6.6 0 1 .4 1 1V20c0 .6-.4 1-1 1C10.6 21 3 13.4 3 4c0-.6.4-1 1-1h3.5c.6 0 1 .4 1 1 0 1.3.2 2.5.6 3.6.1.3 0 .7-.2 1z"/></svg>
    (555) 214 7730
  </div>
</header>

<section class="hero">
  <div class="hero-photo" role="img" aria-label="Engine bay shown half before and half after cleaning"></div>
  <svg class="hero-shape" width="640" height="639" viewBox="0 0 640 639">
    <defs><linearGradient id="heroBlue" x1="0" y1="0" x2="0.4" y2="1"><stop offset="0" stop-color="#0054AA"/><stop offset="1" stop-color="#2a9fd6"/></linearGradient></defs>
    <path d="M0 0H627C650 160 620 360 358 639H0Z" fill="url(#heroBlue)"/>
  </svg>
  <div class="hero-copy">
    <div class="hero-kicker">VELMORA CARWORKS</div>
    <h1 class="hero-title">Automotive Detailing<span>and Cleaning</span></h1>
    <p class="hero-lede">Lorem ipsum dolor sit amet, consectetur adipiscing elit, sed do eiusmod tempor.</p>
  </div>
  <div class="btn btn-outline" style="left:101px;top:375px;width:183px">Book Now
    <svg width="10" height="12" viewBox="0 0 10 12"><path d="M2 1l5 5-5 5" stroke="#fff" stroke-width="2" fill="none"/></svg></div>
  <div class="btn btn-red" style="left:296px;top:375px;width:179px">Call Us Now</div>
  <svg class="slider-arrow" style="left:16px;top:255px" width="24" height="40" viewBox="0 0 24 40"><path d="M20 4L6 20l14 16" stroke="#fff" stroke-width="4" fill="none"/></svg>
  <svg class="slider-arrow" style="left:1164px;top:255px" width="24" height="40" viewBox="0 0 24 40"><path d="M4 4l14 16L4 36" stroke="#fff" stroke-width="4" fill="none"/></svg>
</section>

<div class="sec-title" style="top:789px">
  <div class="sec-kicker" style="color:var(--red)">What We Do</div>
  <div class="sec-heading" style="color:var(--blue-deep)">Our Services</div>
</div>

<article class="service-card" style="left:125px;top:945px;width:293px;height:252px">
  <div class="photo" role="img" aria-label="Hand cleaning a car air vent" style="background:linear-gradient(180deg,#6d6a6b,#2e2c2e)"></div>
  <h3>Automotive Dirt<br>Cleaning</h3>
</article>
<article class="service-card" style="left:776px;top:945px;width:308px;height:252px">
  <div class="photo" role="img" aria-label="Gloved hand cleaning an alloy wheel" style="background:linear-gradient(160deg,#8a8d93,#3a3033 60%,#7d1f24)"></div>
  <h3>Super Dry &amp; Wheel<br>Cleaning</h3>
</article>
<article class="service-featured">
  <h3>Under Carriage &amp;<br>Engine Cleaning</h3>
  <p>Lorem ipsum dolor sit amet, consectetur adipiscing elit, sed do eiusmod tempor incididunt ut labore et dolore</p>
  <div class="btn btn-red">Book Now</div>
</article>

<section class="company">
  <div class="company-oval"><div class="photo" role="img" aria-label="Suspension and undercarriage parts before and after cleaning"></div></div>
  <div class="company-copy">
    <div class="sec-kicker">Who We Are</div>
    <div class="sec-heading">Our Company</div>
    <p class="lede">Lorem ipsum dolor sit amet, consectetur adipiscing elit, sed do eiusmod tempor incididunt ut labore et dolore magna aliqua. Quis ipsum suspendisse ultrices gravida.</p>
    <div class="feature" style="top:206px;left:8px">
      <svg width="52" height="52" viewBox="0 0 52 52" fill="none" stroke="#fff" stroke-width="2"><circle cx="26" cy="26" r="23"/><circle cx="26" cy="26" r="16"/><circle cx="26" cy="26" r="4"/><path d="M26 10v12M26 30v12M10 26h12M30 26h12M15 15l8 8M29 29l8 8M37 15l-8 8M23 29l-8 8"/></svg>
      <div><h4>Fast &amp; Quality Cleaning</h4><p>Lorem ipsum dolor sit amet, consectetur adipiscing</p></div>
    </div>
    <div class="feature" style="top:293px;left:8px">
      <svg width="52" height="52" viewBox="0 0 52 52" fill="none" stroke="#fff" stroke-width="2"><path d="M6 48V30h8v18zM14 32l8-6h8l-6 6h10l8-8"/><circle cx="34" cy="14" r="10"/><path d="M37 10h-4a2 2 0 0 0 0 4h2a2 2 0 0 1 0 4h-4M34 7v3M34 18v3"/></svg>
      <div><h4>Best Price Guarantee</h4><p>Lorem ipsum dolor sit amet, consectetur adipiscing r sit amet</p></div>
    </div>
    <div class="feature" style="top:383px;left:8px">
      <svg width="52" height="52" viewBox="0 0 52 52" fill="none" stroke="#fff" stroke-width="2"><path d="M26 4l18 7v13c0 12-8 20-18 24C16 44 8 36 8 24V11z"/><path d="M18 26l6 6 11-12"/></svg>
      <div><h4>Customer Trusted</h4><p>Lorem ipsum dolor sit amet, consectetur adipiscing</p></div>
    </div>
  </div>
</section>

<div class="sec-title" style="top:2010px">
  <div class="sec-kicker" style="color:var(--blue-deep)">Our Work</div>
  <div class="sec-heading" style="color:var(--red)">Before &amp; After Gallery</div>
  <div class="sec-rule"></div>
</div>
<div class="shot" style="left:48px"><div class="photo" role="img" aria-label="Dirty undercarriage before cleaning" style="background:linear-gradient(160deg,#6f6a63,#4a4844)"></div><div class="label before">BEFORE</div></div>
<div class="shot" style="left:331px"><div class="photo" role="img" aria-label="Clean undercarriage after cleaning" style="background:linear-gradient(160deg,#4d5258,#2c2f34)"></div><div class="label after">AFTER</div></div>
<div class="shot" style="left:615px"><div class="photo" role="img" aria-label="Dirty suspension strut before cleaning" style="background:linear-gradient(160deg,#7a7c7f,#505357)"></div><div class="label before">BEFORE</div></div>
<div class="shot" style="left:895px"><div class="photo" role="img" aria-label="Clean suspension strut after cleaning" style="background:linear-gradient(160deg,#a9abae,#7d4442)"></div><div class="label after">AFTER</div></div>
<div class="dots"><i></i><i></i><i class="on"></i></div>

<section class="testimonials">
  <div class="sec-title" style="top:62px">
    <div class="sec-kicker" style="color:var(--blue-deep);font-size:17px">Testimonials</div>
    <div class="sec-heading" style="color:var(--red);font-size:29px;line-height:34px">What Our Customer Says</div>
    <div class="sec-rule"></div>
  </div>
  <svg class="abs" style="left:70px;top:258px" width="24" height="40" viewBox="0 0 24 40"><path d="M20 4L6 20l14 16" stroke="#8a93a3" stroke-width="3" fill="none"/></svg>
  <svg class="abs" style="left:1106px;top:258px" width="24" height="40" viewBox="0 0 24 40"><path d="M4 4l14 16L4 36" stroke="#8a93a3" stroke-width="3" fill="none"/></svg>
</section>
<div class="quote-card" style="left:133px">
  <blockquote>“Lorem ipsum dolor sit amet, consectetur adipiscing elit, sed do eiusmod tempor incididunt ut labore et dolore magna aliqua. Ut enim ad minim veniam, quis nostrud exercitation ullamco laboris nisi ut aliquip”</blockquote>
  <div class="reviewer"><div class="avatar" role="img" aria-label="Customer portrait"></div><div><b>Dana Ellery</b><span class="stars">★★★★★</span></div></div>
  <div class="quote-mark">”</div>
</div>
<div class="quote-card" style="left:613px">
  <blockquote>“Lorem ipsum dolor sit amet, consectetur adipiscing elit, sed do eiusmod tempor incididunt ut labore et dolore magna aliqua. Ut enim ad minim veniam, quis nostrud exercitation ullamco laboris nisi ut aliquip”</blockquote>
  <div class="reviewer"><div class="avatar" role="img" aria-label="Customer portrait"></div><div><b>Marc Tolland</b><span class="stars">★★★★★</span></div></div>
  <div class="quote-mark">”</div>
</div>

<section class="contact">
  <div class="photo" role="img" aria-label="Hand polishing a black wheel on a red car"></div>
  <svg class="abs" style="left:0;top:0" width="560" height="526" viewBox="0 0 560 526">
    <defs><linearGradient id="contactGrad" x1="0" y1="0" x2="1" y2="1"><stop offset="0" stop-color="#e2442a"/><stop offset=".45" stop-color="#7a4a8c"/><stop offset="1" stop-color="#0b4aa2"/></linearGradient></defs>
    <path d="M0 0H530C575 180 540 350 380 526H0Z" fill="url(#contactGrad)"/>
  </svg>
  <div class="contact-copy">
    <div class="sec-kicker">Get In Touch</div>
    <div class="sec-heading">Contact Us</div>
    <p>Lorem ipsum dolor sit amet, consectetur adipiscing elit, sed do eiusmod tempor incididunt.</p>
    <div class="contact-line" style="top:162px">
      <div class="icon-disc"><svg width="24" height="28" viewBox="0 0 24 28"><path d="M12 1a10 10 0 0 0-10 10c0 8 10 16 10 16s10-8 10-16A10 10 0 0 0 12 1z" fill="#fff"/><circle cx="12" cy="11" r="4" fill="#EC4F4E"/></svg></div>
      <span>Harwell Yard, 12-14 Foundry Lane,<br>Brookford, BF2 7QD</span>
    </div>
    <div class="contact-line" style="top:250px">
      <div class="icon-disc"><svg width="26" height="26" viewBox="0 0 24 24" fill="#fff"><path d="M6.6 10.8a15.1 15.1 0 0 0 6.6 6.6l2.2-2.2c.3-.3.7-.4 1-.2 1.1.4 2.3.6 3.6.6.6 0 1 .4 1 1V20c0 .6-.4 1-1 1C10.6 21 3 13.4 3 4c0-.6.4-1 1-1h3.5c.6 0 1 .4 1 1 0 1.3.2 2.5.6 3.6.1.3 0 .7-.2 1z"/></svg></div>
      <span style="font-size:22px;font-weight:400">(+555) 309 6142</span>
    </div>
  </div>
</section>

<footer class="site-footer">
  <div class="brand"><span class="brand-mark"></span><span class="brand-name">Velmora<br>Carworks</span></div>
  <div class="foot-col" style="left:384px"><h5>Navigation</h5>
    <ul><li>About Us</li><li>Our Services</li><li>Book Now</li><li>Before &amp; after gallery</li></ul></div>
  <div class="foot-col" style="left:620px"><h5>Resources</h5>
    <ul><li>News</li><li>Testimonials</li><li>Support</li><li>Contact Us</li></ul></div>
  <div class="foot-col" style="left:825px"><h5>Contact Us</h5>
    <div class="foot-contact"><span class="small-disc"><svg width="14" height="18" viewBox="0 0 24 28"><path d="M12 1a10 10 0 0 0-10 10c0 8 10 16 10 16s10-8 10-16A10 10 0 0 0 12 1z" fill="#fff"/></svg></span><span>Harwell Yard, 12-14 Foundry Lane,<br>Brookford, BF2 7QD</span></div>
    <div class="foot-contact" style="align-items:center"><span class="small-disc"><svg width="16" height="16" viewBox="0 0 24 24" fill="#fff"><path d="M6.6 10.8a15.1 15.1 0 0 0 6.6 6.6l2.2-2.2c.3-.3.7-.4 1-.2 1.1.4 2.3.6 3.6.6.6 0 1 .4 1 1V20c0 .6-.4 1-1 1C10.6 21 3 13.4 3 4c0-.6.4-1 1-1h3.5c.6 0 1 .4 1 1 0 1.3.2 2.5.6 3.6.1.3 0 .7-.2 1z"/></svg></span><span style="font-size:16px">(+555) 309 6142</span></div>
    <div class="socials" aria-label="Social media links"><i></i><i></i><i></i><i></i></div>
  </div>
  <div class="copyright">Copyright © 2022 Velmora Carworks | All Rights Reserved</div>
</footer>

</div>
</body>
</html>
```